Cybersecurity company is looking for business card.

I need a business card design for our company, we are a cybersecurity company providing advance technology to protect agains any kind of malware. We need a fresh modern design it should communicate modern, technology and growth.

Target Market(s)

Business to business

Industry/Entity Type

Business

Contact Information for Business Card

Should have location, address, fax, mobile, phone, email and website.

Requirements
Must have
• Must follow company's logo color and style. Must have the company's log on its.

```html
<!DOCTYPE html>
<html lang="en">
<head>
<meta charset="UTF-8">
<title>Vaultline Business Card</title>
<link href="https://fonts.googleapis.com/css2?family=Ubuntu:wght@400&display=swap" rel="stylesheet">
<style>
  :root {
    --page: #e8e5e1;
    --card-black: #0b0b0b;
    --pattern-tone: #2a2a2a;
    --panel-red: #b3161c;
    --panel-red-deep: #94121a;
    --ink-white: #f6f3ef;
  }
  * { margin: 0; padding: 0; box-sizing: border-box; }
  html, body {
    width: 1200px;
    height: 700px;
    overflow: hidden;
    background: var(--page);
    font-family: "Ubuntu", sans-serif;
  }
  .card {
    position: absolute;
    left: 100px;
    top: 64px;
    width: 1000px;
    height: 572px;
    background: var(--card-black);
    overflow: hidden;
    box-shadow: 0 10px 30px rgba(0,0,0,0.18);
  }
  .brand-pattern {
    position: absolute;
    inset: 0;
    background: linear-gradient(160deg, var(--pattern-tone) 0%, var(--card-black) 55%, var(--pattern-tone) 100%);
  }
  .contact-panel {
    position: absolute;
    left: 0;
    top: 196px;
    width: 560px;
    height: 376px;
    background: linear-gradient(150deg, var(--panel-red) 0%, var(--panel-red-deep) 100%);
    border-top-right-radius: 18px;
  }
  .corner-mark {
    position: absolute;
    right: 22px;
    top: 16px;
    width: 54px;
    height: 34px;
  }
  .contact-list {
    list-style: none;
    position: absolute;
    left: 46px;
    top: 54px;
  }
  .contact-item {
    display: flex;
    align-items: center;
    gap: 20px;
    height: 58px;
    color: var(--ink-white);
    font-size: 38px;
    letter-spacing: 0.2px;
  }
  .contact-icon {
    width: 34px;
    height: 34px;
    flex: none;
  }
  .contact-icon * {
    fill: none;
    stroke: var(--ink-white);
    stroke-width: 2;
    stroke-linecap: round;
    stroke-linejoin: round;
  }
</style>
</head>
<body>
  <main class="card">
    <div class="brand-pattern" role="img" aria-label="Repeating outlined Vaultline wordmark pattern across the card"></div>

    <section class="contact-panel">
      <svg class="corner-mark" viewBox="0 0 54 34" aria-hidden="true">
        <polygon points="0,0 54,0 54,34" fill="var(--ink-white)"/>
      </svg>

      <ul class="contact-list">
        <li class="contact-item">
          <svg class="contact-icon" viewBox="0 0 34 34" aria-hidden="true">
            <circle cx="17" cy="17" r="14"/>
            <ellipse cx="17" cy="17" rx="6" ry="14"/>
            <line x1="3" y1="17" x2="31" y2="17"/>
          </svg>
          <span class="contact-text">www.vaultline.com</span>
        </li>
        <li class="contact-item">
          <svg class="contact-icon" viewBox="0 0 34 34" aria-hidden="true">
            <rect x="3" y="8" width="28" height="19" rx="1"/>
            <polyline points="3,8 17,19 31,8"/>
          </svg>
          <span class="contact-text">vaultline@mail.com</span>
        </li>
        <li class="contact-item">
          <svg class="contact-icon" viewBox="0 0 34 34" aria-hidden="true">
            <rect x="4" y="13" width="26" height="16" rx="2"/>
            <polyline points="10,13 10,5 24,5 24,13"/>
            <line x1="10" y1="20" x2="24" y2="20"/>
            <line x1="10" y1="24" x2="20" y2="24"/>
          </svg>
          <span class="contact-text">023-55501842</span>
        </li>
        <li class="contact-item">
          <svg class="contact-icon" viewBox="0 0 34 34" aria-hidden="true">
            <path d="M9 4 L13 11 L10 14 C12 19 15 22 20 24 L23 21 L30 25 L27 30 C16 30 4 18 4 7 Z"/>
          </svg>
          <span class="contact-text">+97255500000</span>
        </li>
        <li class="contact-item">
          <svg class="contact-icon" viewBox="0 0 34 34" aria-hidden="true">
            <path d="M17 31 C17 31 7 20 7 13 A10 10 0 0 1 27 13 C27 20 17 31 17 31 Z"/>
            <circle cx="17" cy="13" r="3.5"/>
          </svg>
          <span class="contact-text">12 Harbor Road</span>
        </li>
      </ul>
    </section>
  </main>
</body>
</html>
```